Holm Tasker Dunecrest vehicle wrap

Looking for a partial wrap for our Managed IT Business.
The vehicle is a 2025 Holm Tasker Dunecrest in white.
Our main colour is orange - #f37321.
Wanting to include out website and phone number on it (below)
kestrait.com.au
1300 2 KESTRA
Please take a look at our website to how we brand.
I want to include some of our key services:
Managed IT
Cyber Security
Backup and Disaster Recovery
Looking for maybe a half or 2/3rds wrap.
I have attached my logo, and images of the vehicle.
Here is some text from our website.
Kestra IT is a forward-thinking IT partner dedicated to helping businesses across Australia stay ahead. Founded on a belief that IT should be simple, reliable, and secure, we deliver cloud solutions, cybersecurity, and managed IT services tailored to your needs.
Based in Goulburn, we work with small to medium businesses across industries like trades, professional services, and regional enterprises — simplifying technology so you can focus on what matters most.
At Kestra IT, we pride ourselves on being easy to work with, highly responsive, and committed to real results. We don’t just fix problems — we help prevent them, giving you peace of mind that your IT is in expert hands. Whether you need day-to-day support or a full IT strategy, Kestra IT is here to keep your business moving forward.
Every solution we deliver is backed by honest advice, genuine care, and a deep understanding of what it takes to keep businesses running smoothly.

```html
<!DOCTYPE html>
<html lang="en">
<head>
<meta charset="utf-8">
<title>Kestra IT – Vehicle Wrap Panel</title>
<link rel="stylesheet" href="https://fonts.googleapis.com/css2?family=Outfit:wght@400;500;600;700&display=swap">
<style>
  :root {
    --brand-orange: #f37321;
    --deep-orange: #e2621a;
    --panel-black: #050505;
    --text-white: #ffffff;
    --page-bg: #f2f2f2;
  }
  * { margin: 0; padding: 0; box-sizing: border-box; }
  html, body {
    width: 1200px; height: 734px; overflow: hidden;
    background: var(--page-bg);
    font-family: "Outfit", sans-serif;
  }
  .wrap-panel {
    position: absolute; left: 31px; top: 32px;
    width: 1138px; height: 318px;
    background: var(--panel-black);
    overflow: hidden;
  }
  .circuit-glow-left {
    position: absolute; left: 0; top: 0; width: 330px; height: 318px;
    background:
      radial-gradient(ellipse 95% 80% at 0% 100%, rgba(243,115,33,0.85) 0%, rgba(243,115,33,0.35) 40%, rgba(243,115,33,0) 75%),
      linear-gradient(135deg, rgba(243,115,33,0.18) 0%, rgba(243,115,33,0) 60%);
  }
  .circuit-glow-right {
    position: absolute; left: 905px; top: 135px; width: 215px; height: 183px;
    background: radial-gradient(ellipse 60% 55% at 55% 45%, rgba(243,115,33,0.32) 0%, rgba(243,115,33,0) 75%);
  }
  .shield-emblem {
    position: absolute; left: 300px; top: 140px; width: 200px; height: 160px;
    background: radial-gradient(circle at 50% 50%, rgba(243,115,33,0.55) 0%, rgba(243,115,33,0.18) 30%, rgba(243,115,33,0.05) 55%, rgba(243,115,33,0) 72%);
  }
  .headline {
    position: absolute; left: 466px; top: 176px;
    font-size: 18px; line-height: 23px; font-weight: 600;
    color: var(--text-white); letter-spacing: -0.2px;
  }
  .headline .headline-accent { color: var(--brand-orange); font-weight: 400; }
  .service-list {
    position: absolute; top: 262px; list-style: none;
    font-size: 11px; line-height: 19px; color: var(--text-white);
  }
  .service-list li { display: flex; align-items: flex-start; gap: 8px; }
  .service-list svg { flex: none; margin-top: 4px; }
  .services-left { left: 466px; }
  .services-right { left: 565px; }
  .services-right li span { line-height: 14px; margin-top: 3px; }
  .brand-name {
    position: absolute; left: 694px; top: 168px;
    font-size: 36px; font-weight: 700; color: var(--text-white);
    letter-spacing: -1px; line-height: 44px;
  }
  .web-tag {
    position: absolute; left: 694px; top: 225px; width: 124px; height: 26px;
    background: var(--brand-orange); color: var(--text-white);
    display: flex; align-items: center; justify-content: center; gap: 5px;
    font-size: 13px; font-weight: 500;
  }
</style>
</head>
<body>
  <section class="wrap-panel" aria-label="Kestra IT vehicle wrap side panel">
    <div class="circuit-glow-left" role="img" aria-label="Orange circuit board traces glowing from the lower left corner"></div>
    <div class="circuit-glow-right" role="img" aria-label="Orange circuit board traces on the right"></div>
    <div class="shield-emblem" role="img" aria-label="Orange security shield with a keyhole and soft radiating rings"></div>

    <h1 class="headline">Simplifying IT,<br><span class="headline-accent">Securing Your Future</span></h1>

    <ul class="service-list services-left">
      <li><svg width="11" height="10" viewBox="0 0 11 10"><path d="M1 5.5 L4 8.5 L10 1" fill="none" stroke="#f37321" stroke-width="1.8"/></svg><span>Managed IT</span></li>
      <li><svg width="11" height="10" viewBox="0 0 11 10"><path d="M1 5.5 L4 8.5 L10 1" fill="none" stroke="#f37321" stroke-width="1.8"/></svg><span>Cyber Security</span></li>
    </ul>
    <ul class="service-list services-right">
      <li><svg width="11" height="10" viewBox="0 0 11 10"><path d="M1 5.5 L4 8.5 L10 1" fill="none" stroke="#f37321" stroke-width="1.8"/></svg><span>Backup &amp; Disaster<br>Recovery</span></li>
    </ul>

    <div class="brand-name">Kestra IT</div>
    <div class="web-tag">
      <svg width="7" height="9" viewBox="0 0 7 9"><path d="M0 0 L7 5 L4 5 L5.5 8.5 L4.3 9 L2.8 5.6 L0 7.5 Z" fill="#ffffff"/></svg>
      <span>kestrait.com.au</span>
    </div>
  </section>
</body>
</html>
```